Gentleman's grooming products require a business card

I need a business card that incorporates the logo [ or parts of ] that we had Pixel Hive design for us as uploaded.

We sell online, mens grooming products including moustache waxes, beard oils and shaving accessories.
We want a card that is classy, professional and a card that shouts mens products.

Target Market(s)

Young professional male market

Industry/Entity Type

Business

Contact Information for Business Card

Ross and Edith Carwell
Lather and Lore
Purveyors of gentleman's stiffeners and grooming requisites
M :0418529647
E : ross@latherandlore.com.au
E : edith@latherandlore.com.au
E : sales@theblokesbalmery.com.au

W : www.latherandlore.com.au

Requirements
Must have
• Class
Nice to have
• Professionalism

```html
<!DOCTYPE html>
<html lang="en">
<head>
<meta charset="utf-8">
<title>Lather and Lore — Business Card</title>
<link rel="stylesheet" href="https://fonts.googleapis.com/css2?family=Cinzel:wght@400&family=Poiret+One&display=swap">
<style>
  :root {
    --card-black: #000000;
    --panel-black: #0d0d0d;
    --ink-white: #ffffff;
  }
  html, body {
    margin: 0;
    padding: 0;
    width: 1200px;
    height: 686px;
    overflow: hidden;
    background: var(--card-black);
  }
  .card {
    position: relative;
    width: 1200px;
    height: 686px;
    background: var(--card-black);
    color: var(--ink-white);
    overflow: hidden;
  }
  .brand-panel {
    position: absolute;
    left: 76px;
    top: 0;
    width: 1050px;
    height: 481px;
    background: var(--panel-black);
  }
  .rule {
    position: absolute;
    left: 175px;
    width: 846px;
    height: 3px;
    background: var(--ink-white);
  }
  .rule--top { top: 204px; }
  .rule--bottom { top: 377px; }
  .brand-name {
    position: absolute;
    left: 175px;
    top: 252px;
    width: 846px;
    margin: 0;
    text-align: center;
    font-family: "Cinzel", serif;
    font-weight: 400;
    font-size: 80px;
    line-height: 1;
    letter-spacing: 2px;
    color: var(--ink-white);
  }
  .tagline {
    position: absolute;
    left: 175px;
    top: 409px;
    width: 846px;
    margin: 0;
    text-align: center;
    font-family: "Cinzel", serif;
    font-size: 17px;
    letter-spacing: 2px;
    color: var(--ink-white);
    white-space: nowrap;
  }
  .owners {
    position: absolute;
    left: 29px;
    top: 475px;
    width: 400px;
    margin: 0;
    text-align: center;
    font-family: "Poiret One", sans-serif;
    font-size: 46px;
    line-height: 57px;
    letter-spacing: 1.5px;
    color: var(--ink-white);
    -webkit-text-stroke: 0.8px var(--ink-white);
    white-space: nowrap;
  }
  .owners span { display: block; }
  .contact-list {
    position: absolute;
    left: 430px;
    top: 454px;
    width: 740px;
    margin: 0;
    padding: 0;
    list-style: none;
    text-align: center;
    font-family: "Poiret One", sans-serif;
    font-size: 38px;
    line-height: 40.5px;
    letter-spacing: 2px;
    color: var(--ink-white);
    -webkit-text-stroke: 0.3px var(--ink-white);
    white-space: nowrap;
  }
</style>
</head>
<body>
  <main class="card">
    <div class="brand-panel"></div>
    <div class="rule rule--top"></div>
    <h1 class="brand-name">Lather and Lore</h1>
    <div class="rule rule--bottom"></div>
    <p class="tagline">PURVEYORS OF GENTLEMEN’S WAXES, BALMS AND GROOMING REQUISITES</p>

    <p class="owners">
      <span>Ross</span>
      <span>&amp;</span>
      <span>Edith Carwell</span>
    </p>

    <ul class="contact-list">
      <li>M:0418529647</li>
      <li>E: ross@latherandlore.com.au</li>
      <li>E: edith@latherandlore.com.au</li>
      <li>E: sales@theblokesbalmery.com.au</li>
      <li>W: www.latherandlore.com.au</li>
    </ul>
  </main>
</body>
</html>
```